Personal Business card and maybe logo or graphic?

I would like a card to give out like you would a business card, however I am not promoting a business, it is just for my personal details.

I have no brand and no logo to worry about.

I would like some images or a logo of some kind or a graphic so the card has some excitement about it.

I am happy if you wish to create a logo/graphic that represents my name, I have seen someone with just their initials as a graphic so for me PH, however I am happy for you to create anything you wish, it does not have to relate to me just make the card look fun and still professional.

Please use the details

Peter Hadley

Ashcombe Lodge
9 The Mews
Fern Close
Bournemouth
Dorset
BH4 2QT

+44 (0)7812 604258
peter@hadleypost.example
linkedin.example/in/hadleypeter

looking for a mix between fun, fresh , young whilst being professional

I am new to this and am looking for you to guide me through the process please ask questions and ideas

I am just tidying up my brief as I am starting to understand more. hope it has not confused anyone
Updates

Reason: I have not had time to review or comment due to personal issues sorry

Hi,

to help would you be so kind as to use these sample details on the card

I am uk based and a few designs have us details which look different

Peter Hadley

Ashcombe lodge

9 The Mews

Fern Close

Bournemouth

Dorset

BH4 2QT

+44 (0)7812 604258

peter@hadleypost.example

many thanks hope that is ok and not too much trouble!

regards

Pim

My are of expertise is IT management / IT Consultancy, incase you wish to incorporate any graphics

My job was that of CIO (Chief Information Officer) or another term is Head of IT

just advising incase this gives any assistance as one designer has asked s may be useful to others

thanks                                   

just thought I have had a look and the UK size for a business card seems to be as per below

I thought I would mention as I guess the US size may be different and other countries too

I found these sizes on Cardforge but guess most companies will be similar

that said maybe you can advise me

I have no idea what cardforge is like so not sure where to get cards made, will figure that out later I guess but I assume dimensions are important for the design

thanks

 

Document Trim Size    

            Horizontal        

        85 x 55 mm           

1004 x 650 pixels           

            Vertical        

        55 x 85 mm           

650 x 1004 pixels           

        Full Bleed Size    

            Horizontal        

        88 x 58 mm           

1039 x 685 pixels           

            Vertical        

        58 x 88 mm           

685 x 1039 pixels           

 many thanks

Target Market(s)

Professional and personal contacts

Industry/Entity Type

Business

```html
<!DOCTYPE html>
<html lang="en">
<head>
<meta charset="utf-8">
<title>Peter Hadley – Business Card</title>
<link rel="stylesheet" href="https://fonts.googleapis.com/css2?family=Roboto:wght@300;400&display=swap">
<style>
  :root {
    --stage-light: #ffffff;
    --stage-edge: #d6d6d6;
    --slate: #58585a;
    --tangerine: #f15a2b;
    --paper: #ffffff;
    --muted: #c9c9cb;
  }
  html, body {
    margin: 0;
    width: 1200px;
    height: 1200px;
    overflow: hidden;
  }
  body {
    background: radial-gradient(circle at 50% 50%, var(--stage-light) 35%, var(--stage-edge) 100%);
    font-family: "Roboto", Arial, sans-serif;
    position: relative;
  }
  .card {
    position: absolute;
    left: 350px;
    top: 170px;
    width: 502px;
    height: 876px;
    background: var(--slate);
    border-bottom-right-radius: 135px;
    overflow: hidden;
  }
  .card-shapes {
    position: absolute;
    inset: 0;
    width: 502px;
    height: 876px;
  }
  .identity {
    position: absolute;
    right: 30px;
    top: 30px;
    text-align: right;
    color: var(--paper);
  }
  .identity-name {
    margin: 0;
    font-size: 27px;
    font-weight: 400;
    line-height: 1.1;
  }
  .identity-role {
    margin: 2px 0 0;
    font-size: 18px;
    font-weight: 300;
    letter-spacing: 4px;
    color: var(--muted);
  }
  .monogram {
    position: absolute;
    left: 161px;
    top: 293px;
    width: 172px;
    height: 172px;
    display: flex;
    align-items: center;
    justify-content: center;
    color: var(--tangerine);
    font-size: 72px;
    font-weight: 400;
    letter-spacing: 2px;
  }
  .contact-list {
    position: absolute;
    left: 46px;
    top: 660px;
    width: 410px;
    margin: 0;
    padding: 0;
    list-style: none;
  }
  .contact-item {
    display: flex;
    align-items: center;
    height: 44px;
    border-bottom: 2px solid var(--paper);
    color: var(--paper);
    font-size: 20px;
    font-weight: 400;
    letter-spacing: 0.3px;
    white-space: nowrap;
  }
  .contact-item + .contact-item { margin-top: 1px; }
  .contact-icon {
    width: 34px;
    height: 30px;
    margin: 0 20px 0 18px;
    flex: none;
  }
</style>
</head>
<body>
  <article class="card">
    <svg class="card-shapes" viewBox="0 0 502 876" aria-hidden="true">
      <path fill="var(--tangerine)" d="M0 224 L222 424 L502 153 L502 876 L0 876 Z"/>
      <circle fill="var(--paper)" cx="247" cy="379" r="86"/>
    </svg>

    <header class="identity">
      <h1 class="identity-name">Peter Hadley</h1>
      <p class="identity-role">IT Consultant</p>
    </header>

    <div class="monogram">PH</div>

    <ul class="contact-list">
      <li class="contact-item">
        <svg class="contact-icon" viewBox="0 0 34 30" aria-hidden="true">
          <rect x="1" y="3" width="32" height="7" rx="3" fill="var(--paper)"/>
          <rect x="5" y="11" width="24" height="18" rx="2" fill="var(--paper)"/>
          <g fill="var(--tangerine)">
            <rect x="9" y="15" width="4" height="3"/><rect x="15" y="15" width="4" height="3"/><rect x="21" y="15" width="4" height="3"/>
            <rect x="9" y="21" width="4" height="3"/><rect x="15" y="21" width="4" height="3"/><rect x="21" y="21" width="4" height="3"/>
          </g>
        </svg>
        <span>+44 (0)7812 604258</span>
      </li>
      <li class="contact-item">
        <svg class="contact-icon" viewBox="0 0 34 30" aria-hidden="true">
          <rect x="1" y="5" width="32" height="21" fill="var(--paper)"/>
          <path d="M1 5 L17 18 L33 5" fill="none" stroke="var(--tangerine)" stroke-width="2"/>
          <path d="M1 26 L13 15 M33 26 L21 15" fill="none" stroke="var(--tangerine)" stroke-width="2"/>
        </svg>
        <span>peter@hadleypost.example</span>
      </li>
      <li class="contact-item">
        <svg class="contact-icon" viewBox="0 0 34 30" aria-hidden="true">
          <path d="M17 29 C10 20 7 15 7 11 A10 10 0 0 1 27 11 C27 15 24 20 17 29 Z" fill="var(--paper)"/>
          <circle cx="17" cy="11" r="4" fill="var(--tangerine)"/>
        </svg>
        <span>9 The Mews, Bournemouth BH4 2QT</span>
      </li>
    </ul>
  </article>
</body>
</html>
```